QUILLO Q

we need a label for a polyacetate bag. The product is a disposable multi use cloth. These normally come in packs of 5- 10, we want to provide a greater quantity. So that the QUILLO refers to the quantity of cloths and not the size of the cloth. We want to bring excitement to an old and boring product.
The label size: 7 inches across x 9 inches long ( subject to bag manufacture's approval)
Colours : No more than 3
Name of the item is: QUILLO PAK
The number in each pack is : 50 ( This number should appear on the label)
The words: Re-useable, Multi-Purpose, Super Absorbent Cloths; KEEP OUT OF THE REACH OF CHILDREN, must appear on the label.
DIMENSIONS: 21X 14" ( 53cm X 35cm )
The label should not be totally occlusive, the cloth must be seen through clear parts of the label. Consequently the colours of the cloths, Blue, Pink or Green should be taken into account when making the choice of colors and quantity of color/ink needed for the label.
The efficient use of color and the quantity of ink required for the design is important. The cost to print the label must not exceed the value of this product.

```html
<!DOCTYPE html>
<html lang="en">
<head>
<meta charset="utf-8">
<title>QUILLO PAK – Cloth Pack Label</title>
<link rel="stylesheet" href="https://fonts.googleapis.com/css2?family=Montserrat:wght@800&display=swap">
<style>
  :root {
    --label-blue: #0a7cf2;
    --label-orange: #f9a606;
    --label-white: #ffffff;
    --page-bg: #ffffff;
  }
  html, body {
    margin: 0;
    padding: 0;
    width: 1200px;
    height: 1000px;
    overflow: hidden;
    background: var(--page-bg);
  }
  .canvas {
    position: relative;
    width: 1200px;
    height: 1000px;
  }
  .pack-label {
    position: absolute;
    left: 100px;
    top: 146px;
    width: 1000px;
    height: 707px;
    display: block;
  }
  .label-ground { fill: var(--label-blue); }
  .label-text {
    font-family: "Montserrat", Arial, sans-serif;
    font-weight: 800;
  }
  .product-name { fill: var(--label-white); }
  .pack-count { fill: var(--label-orange); }
  .feature-line { fill: var(--label-white); }
  .feature-dot { fill: var(--label-orange); }
  .absorbent-line { fill: var(--label-orange); }
  .safety-note { fill: var(--label-white); }
</style>
</head>
<body>
<main class="canvas">
  <svg class="pack-label" viewBox="0 0 1000 707" xmlns="http://www.w3.org/2000/svg" aria-label="QUILLO PAK 50 cloth pack label">
    <rect class="label-ground" x="0" y="0" width="1000" height="707"/>

    <text class="label-text product-name" x="470" y="128" font-size="104" text-anchor="middle">QUILLO PAK</text>

    <text class="label-text pack-count" x="470" y="560" font-size="540" text-anchor="middle">50</text>

    <text class="label-text feature-line" x="470" y="620" font-size="46" text-anchor="middle">RE-USEABLE<tspan class="feature-dot">•</tspan>MULTI-PURPOSE</text>

    <text class="label-text absorbent-line" x="470" y="668" font-size="40" text-anchor="middle">SUPER ABSORBENT CLOTHS</text>

    <text class="label-text safety-note" x="0" y="0" font-size="16" text-anchor="middle" transform="translate(978 340) rotate(-90)">KEEP OUT OF THE REACH OF CHILDREN</text>
  </svg>
</main>
</body>
</html>
```